CupTradeHub

-
Below info still applicable but I wanted to highlight the point that I am looking for a design similar to the style linkloop+ with the mentioned color scheme (below). If you do that then the project is yours, I'm happy with an almost clone design. I know this is a completely different type of app but what I mean is:
- The listings to look like the linkloop+ widgets (i.e. blocks, three column, and clearly seperated)
- Adverts and listings mixed together in the results set
- Prominent listings to take up 2 or 3 of the columns instead, non prominent ones to take up 1.
- Clear spacing between the listings, as with linkloop+ widgets
- Clear seperation between menu and widgets as with linkloop+
- Search/filters and category filters on the right or left, as with linkloop+
Again, if this is not clear I want it LIKE LINKLOOP+, so far had stock template designs that weren't anything like this.
Linkloop+ is not the only site I listed for inspiration, but I think its easier at this point to just say clone the damn thing, and re purpose it for coffee. We will make additional changes at development time to make it distinct and incorporate some of the other things we were looking for.
-
Hi All,
I'm looking to get designs for a new site that allows coffee roasters, and barista equipment suppliers to sell their goods to coffee shops via an auction site. So essentially B2B bidnest targeted at the coffee market.
Pages required:
All pages:
- Logo
- Login/register links (or my account if logged in)
- links to Contact us, FAQs, Advertise with us
Homepage:
- Search bar
- List of filter categories
- Latest products section
- Advertising section
Search page:
- Listings (Image, price (buy now or current bid), postage price, no bids, time remaining to bid)
- Advertising
Listing page
- Same listing info as above but with full description, multipule images to select from, time ending and and a bid form (enter amount) or buy now button.
Login page
- Username/Password
- Alternative login via Friendora
My account:
- Link to add listings
- List of current listings
- List of current bids
- Link to purchase history
Add a listing:
- Form page to add a listing
- Requires
- Images uploads (drag to upload, as well as normal)
- Title field
- Description field
- Amount field
- Quantity field
- Postage amount field
- Category Drop down field
- End date/time picker field
That's it for functionality, with regards to design this needs to be designed in a way that is compatible with scaffoldr components (http://chirpnet.codehost.example/scaffoldr/), though scaffoldr is highly customizable so don't feel too restricted.
Styles/colours:
Site layout should be clean, and clear utilizing white space well i.e.
- http://shrt.example/qpWmT
- http://shrt.example/VbRdK
- https://circles.linkloop.example/
Also VERY much like the vantasoft "tiler" style design i.e. square boxes. If you know what I mean by this then cool, if not don't worry about it.
The logo on the other hand should have and earthy, organic feel to it.
Also, please only use fonts available from typevault fonts (http://www.typevault.example/fonts/).

```html
<!DOCTYPE html>
<html lang="en">
<head>
<meta charset="utf-8">
<title>CupTradeHub</title>
<link rel="stylesheet" href="https://fonts.googleapis.com/css2?family=Arimo:wght@400;700&display=swap">
<style>
:root{
  --brown:#9a5534;
  --brown-dark:#7f4327;
  --blue:#3d76d6;
  --orange:#d46b3b;
  --sidebar:#f1f1f1;
  --line:#d4d4d4;
  --ad:#d6d6d6;
  --text:#444;
  --muted:#666;
  --white:#fff;
}
*{box-sizing:border-box;margin:0;padding:0}
html,body{width:1200px;height:778px;overflow:hidden}
body{font-family:"Arimo",Arial,sans-serif;color:var(--text);background:var(--white);position:relative}

.site-header{position:absolute;left:0;top:0;width:1200px;height:110px;background:linear-gradient(#fafafa,#eeeeee);border-bottom:1px solid var(--line)}
.brand{position:absolute;left:14px;top:12px;display:flex;align-items:center;gap:10px}
.brand-mark{width:80px;height:80px;border-radius:50%;background:var(--brown)}
.brand-name{font-size:31px;color:var(--brown);font-weight:400;letter-spacing:-.3px}
.top-links{position:absolute;right:14px;top:10px;display:flex;font-size:14px;color:var(--muted)}
.top-links a{color:inherit;text-decoration:none;padding:0 17px;border-left:1px solid #bbb}
.top-links a:first-child{border-left:0}
.top-links a:last-child{padding-right:0}
.btn-auth{position:absolute;top:53px;height:41px;border-radius:4px;color:#fff;font-weight:700;font-size:16px;display:flex;align-items:center;justify-content:center;box-shadow:0 1px 2px rgba(0,0,0,.3)}
.btn-login{left:884px;width:125px;background:linear-gradient(#a5603d,#8a4a2b)}
.btn-register{left:1034px;width:150px;background:linear-gradient(#4a8ae0,#2f68c6)}

.sidebar{position:absolute;left:0;top:111px;width:447px;height:667px;background:var(--sidebar);border-right:1px solid var(--line)}
.sidebar-title{position:absolute;left:14px;top:30px;font-size:26px;font-weight:400;color:var(--brown)}
.field{position:absolute;background:linear-gradient(#fdfdfd,#e9e9e9);border:1px solid #cfcfcf;border-radius:3px;font-size:14px;color:#555;display:flex;align-items:center;justify-content:center}
.field::after{content:"";position:absolute;right:12px;top:50%;margin-top:-3px;border:5px solid transparent;border-top:6px solid #555;border-bottom:0}
.search-input{position:absolute;left:14px;top:85px;width:420px;height:41px;background:#fff;border:1px solid #c9c9c9;border-radius:3px;font-size:15px;color:#aaa;padding-left:14px;display:flex;align-items:center}
.search-input svg{position:absolute;right:10px;top:9px}
.range-label{position:absolute;left:15px;top:270px;font-size:14px;color:var(--muted)}
.range-scale{position:absolute;left:14px;top:304px;width:420px;height:14px;font-size:13px;color:#999}
.range-scale span{position:absolute;transform:translateX(-50%)}
.range-ticks{position:absolute;left:20px;top:322px;width:406px;height:8px}
.range-track{position:absolute;left:14px;top:332px;width:420px;height:10px;border-radius:4px;background:#ddd;border:1px solid #ccc}
.range-track::before{content:"";position:absolute;left:4px;right:4px;top:3px;height:2px;background:var(--brown-dark)}
.range-track::after{content:"";position:absolute;left:264px;right:4px;top:3px;height:2px;background:#333}
.handle{position:absolute;top:347px}
.btn-search{position:absolute;left:14px;top:400px;width:200px;height:45px;border-radius:3px;background:linear-gradient(#9a5534,#7e4226);color:#fff;font-size:17px;display:flex;align-items:center;padding-left:58px}
.btn-search .icon{position:absolute;left:6px;top:6px;width:33px;height:33px;border-radius:50%;background:#5f301a}
.btn-clear{position:absolute;left:230px;top:400px;width:204px;height:45px;border-radius:3px;background:linear-gradient(#fdfdfd,#e4e4e4);border:1px solid #ccc;font-size:17px;color:#666;display:flex;align-items:center;justify-content:center}
.ad{position:absolute;background:var(--ad);color:#555;display:flex;flex-direction:column;align-items:center;justify-content:center;line-height:1.05}
.ad strong{font-weight:400}
.ad-side{left:14px;top:472px;width:418px;height:179px}
.ad-side strong{font-size:25px}
.ad-side span{font-size:17px}

.main{position:absolute;left:447px;top:111px;width:753px;height:667px}
.ad-top{left:11px;top:12px;width:730px;height:60px}
.ad-top strong{font-size:25px}
.ad-top span{font-size:17px}
.section-title{position:absolute;left:14px;top:82px;font-size:22px;font-weight:400;color:var(--brown)}
.pager{position:absolute;right:12px;top:80px;display:flex;align-items:center;gap:4px;font-size:14px;color:var(--muted)}
.pager span{margin-right:6px}
.pager-btn{width:29px;height:28px;border:1px solid #ccc;border-radius:2px;background:linear-gradient(#fff,#ececec);display:flex;align-items:center;justify-content:center}

.listings{position:absolute;left:12px;top:117px;display:grid;grid-template-columns:359px 359px;grid-auto-rows:150px;gap:11px 11px}
.listing{position:relative;color:#fff;font-size:13px}
.listing-blue{background:var(--blue)}
.listing-orange{background:var(--orange)}
.listing-photo{position:absolute;left:11px;top:12px;width:164px;height:126px;background:#fff;padding:4px}
.listing-photo div{width:100%;height:100%}
.listing-label{position:absolute;left:188px;top:21px;font-size:15px}
.price-tag{position:absolute;left:267px;top:11px;width:83px;height:32px;background:#fff;color:#222;font-size:20px;display:flex;align-items:center;justify-content:flex-end;padding-right:10px;clip-path:polygon(14px 0,100% 0,100% 100%,14px 100%,0 50%)}
.price-tag::before{content:"";position:absolute;left:10px;top:13px;width:5px;height:5px;border-radius:50%;background:#bbb}
.listing-meta{position:absolute;left:188px;top:53px;width:165px;line-height:15px}
.listing-meta dt{position:absolute;left:0}
.listing-meta dd{margin-left:107px;height:20px}
.listing-meta dd.tall{height:auto;padding-top:15px}

.site-footer{position:absolute;left:0;bottom:0;width:753px;height:63px;background:#ececec;border-top:1px solid #ddd;font-size:14px;color:#555;display:flex;align-items:center;justify-content:space-between;padding:0 14px}
</style>
</head>
<body>
<header class="site-header">
  <div class="brand"><div class="brand-mark"></div><span class="brand-name">CupTradeHub</span></div>
  <nav class="top-links"><a href="#">Contact us</a><a href="#">FAQ</a><a href="#">Advertise with us</a></nav>
  <a class="btn-auth btn-login">Login</a>
  <a class="btn-auth btn-register">Register</a>
</header>

<aside class="sidebar">
  <h2 class="sidebar-title">Search Products</h2>
  <div class="search-input">Enter the keyword to start the search
    <svg width="24" height="22" viewBox="0 0 24 22"><circle cx="9" cy="8" r="6" fill="none" stroke="#999" stroke-width="2"/><path d="M13.5 12.5l7 6" stroke="#999" stroke-width="3" stroke-linecap="round"/></svg>
  </div>
  <div class="field" style="left:14px;top:140px;width:201px;height:40px;padding-right:24px">Select the Location</div>
  <div class="field" style="left:234px;top:140px;width:201px;height:40px;padding-right:24px">Select the category</div>
  <div class="field" style="left:14px;top:202px;width:421px;height:41px;padding-right:24px">Select the Brand / Comapany / Industry</div>
  <p class="range-label">Select the price range ($)</p>
  <div class="range-scale">
    <span style="left:6px">0</span><span style="left:75px">50</span><span style="left:143px">100</span><span style="left:211px">150</span><span style="left:276px">200</span><span style="left:345px">250</span><span style="left:411px">300</span>
  </div>
  <svg class="range-ticks" viewBox="0 0 406 8"><g stroke="#bbb" stroke-width="1">
    <path d="M0 0v8M13 4v4M27 4v4M40 4v4M54 4v4M68 0v8M81 4v4M95 4v4M108 4v4M122 4v4M136 0v8M149 4v4M163 4v4M176 4v4M190 4v4M203 0v8M217 4v4M230 4v4M244 4v4M257 4v4M271 0v8M284 4v4M298 4v4M311 4v4M325 4v4M338 0v8M352 4v4M365 4v4M379 4v4M392 4v4M406 0v8"/></g></svg>
  <div class="range-track"></div>
  <svg class="handle" style="left:14px" width="16" height="23" viewBox="0 0 16 23"><path d="M8 1L15 7V22H1V7Z" fill="#d9d9d9" stroke="#999"/></svg>
  <svg class="handle" style="left:270px" width="16" height="23" viewBox="0 0 16 23"><path d="M8 1L15 7V22H1V7Z" fill="#d9d9d9" stroke="#999"/></svg>
  <a class="btn-search"><span class="icon"><svg width="33" height="33" viewBox="0 0 33 33"><circle cx="14" cy="14" r="5" fill="none" stroke="#fff" stroke-width="2"/><path d="M18 18l6 6" stroke="#fff" stroke-width="3" stroke-linecap="round"/></svg></span>Search Product</a>
  <a class="btn-clear">Clear Fields</a>
  <div class="ad ad-side"><strong>350 X 150</strong><span>Advertise Here</span></div>
</aside>

<main class="main">
  <div class="ad ad-top"><strong>610 X 50</strong><span>Advertise Here</span></div>
  <h2 class="section-title">Latest Products</h2>
  <div class="pager"><span>Showing 6 of 30</span>
    <a class="pager-btn"><svg width="8" height="12" viewBox="0 0 8 12"><path d="M6 1L1 6l5 5" fill="none" stroke="#999" stroke-width="1.5"/></svg></a>
    <a class="pager-btn"><svg width="8" height="12" viewBox="0 0 8 12"><path d="M2 1l5 5-5 5" fill="none" stroke="#777" stroke-width="1.5"/></svg></a>
  </div>

  <section class="listings">
    <article class="listing listing-blue">
      <div class="listing-photo"><div role="img" aria-label="Roasted coffee beans" style="background:radial-gradient(circle at 40% 40%,#7a4a2e,#3a2012)"></div></div>
      <span class="listing-label">Price</span><span class="price-tag">220 $</span>
      <dl class="listing-meta"><dt>Posted Price</dt><dd>: 200$</dd><dt>Bids</dt><dd>: 450</dd><dt>Time remaining<br>to bid</dt><dd class="tall">: 20:30:21</dd></dl>
    </article>
    <article class="listing listing-orange">
      <div class="listing-photo"><div role="img" aria-label="Two coffee packets" style="background:linear-gradient(90deg,#2c3f6e,#8a8a7a 55%,#c9b77c)"></div></div>
      <span class="listing-label">Price</span><span class="price-tag">220 $</span>
      <dl class="listing-meta"><dt>Posted Price</dt><dd>: 200$</dd><dt>Bids</dt><dd>: 450</dd><dt>Time remaining<br>to bid</dt><dd class="tall">: 20:30:21</dd></dl>
    </article>
    <article class="listing listing-orange">
      <div class="listing-photo"><div role="img" aria-label="Black coffee bag" style="background:linear-gradient(90deg,#fff 28%,#1d1d1d 28%,#2a2a2a 72%,#fff 72%)"></div></div>
      <span class="listing-label">Price</span><span class="price-tag">220 $</span>
      <dl class="listing-meta"><dt>Posted Price</dt><dd>: 200$</dd><dt>Bids</dt><dd>: 450</dd><dt>Time remaining<br>to bid</dt><dd class="tall">: 20:30:21</dd></dl>
    </article>
    <article class="listing listing-blue">
      <div class="listing-photo"><div role="img" aria-label="Coffee machine with cups" style="background:radial-gradient(ellipse at 60% 55%,#c4343a,#8a3a3a 40%,#fff 75%)"></div></div>
      <span class="listing-label">Price</span><span class="price-tag">220 $</span>
      <dl class="listing-meta"><dt>Posted Price</dt><dd>: 200$</dd><dt>Bids</dt><dd>: 450</dd><dt>Time remaining<br>to bid</dt><dd class="tall">: 20:30:21</dd></dl>
    </article>
    <article class="listing listing-blue">
      <div class="listing-photo"><div role="img" aria-label="Kraft paper coffee bag" style="background:linear-gradient(90deg,#fff 26%,#c79a5c 26%,#a97a40 74%,#fff 74%)"></div></div>
      <span class="listing-label">Price</span><span class="price-tag">220 $</span>
      <dl class="listing-meta"><dt>Posted Price</dt><dd>: 200$</dd><dt>Bids</dt><dd>: 450</dd><dt>Time remaining<br>to bid</dt><dd class="tall">: 20:30:21</dd></dl>
    </article>
    <article class="listing listing-orange">
      <div class="listing-photo"><div role="img" aria-label="Cup of coffee on saucer with beans" style="background:radial-gradient(ellipse at 50% 62%,#6b4630,#c9b8a8 45%,#fff 70%)"></div></div>
      <span class="listing-label">Price</span><span class="price-tag">220 $</span>
      <dl class="listing-meta"><dt>Posted Price</dt><dd>: 200$</dd><dt>Bids</dt><dd>: 450</dd><dt>Time remaining<br>to bid</dt><dd class="tall">: 20:30:21</dd></dl>
    </article>
  </section>

  <footer class="site-footer"><span>© CupTradeHub</span><span>All Rights Reserved</span></footer>
</main>
</body>
</html>
```